Corvane semiconductor corporate presentation

We need a new template with some fresh design elements as we've just announced the acquisition of a new company. Similarly, the backend of the ppt is not set up correctly - and doesn't format properly when dropping in copied text. Attached is the powerpoint presentation/ template as it stands today.
Industry/Entity Type
It Company
Font styles to use
Other font styles liked:
- Arial
Look and feel
Each slider illustrates characteristics of the customer's brand and the style your logo design should communicate.

```html
<!DOCTYPE html>
<html lang="en">
<head>
<meta charset="utf-8">
<title>Corvane semiconductor – Pillars of our Strategy</title>
<link href="https://fonts.googleapis.com/css2?family=Roboto:wght@400;500;700;900&display=swap" rel="stylesheet">
<style>
  :root{
    --stage:#00b9ea;
    --slide:#ffffff;
    --heading:#59606b;
    --accent:#3d94f2;
    --body-blue:#1f6fd8;
    --muted:#6b717b;
    --stack-light:#58b0f5;
    --stack-dark:#0f56b0;
  }
  *{margin:0;padding:0;box-sizing:border-box}
  html,body{width:1200px;height:1200px;overflow:hidden}
  body{background:var(--stage);font-family:"Roboto",Arial,sans-serif;position:relative}
  .slide{position:absolute;left:40px;top:285px;width:1120px;height:630px;background:var(--slide);box-shadow:0 20px 50px rgba(0,60,100,.25);overflow:hidden}
  .slide__rule{position:absolute;left:40px;top:36px;width:3px;height:90px;background:var(--accent)}
  .slide__title{position:absolute;left:70px;top:40px;font-size:46px;font-weight:900;color:var(--heading);letter-spacing:-.5px}
  .slide__title em{font-style:normal;color:var(--accent)}
  .slide__subtitle{position:absolute;left:70px;top:104px;font-size:16px;color:var(--muted)}
  .pillar{position:absolute;width:280px}
  .pillar__name{font-size:20px;font-weight:700;color:var(--heading);margin-bottom:6px}
  .pillar__text{font-size:15px;font-weight:500;color:var(--body-blue);line-height:1.3}
  .pillar--left{text-align:right}
  .pillar__icon{position:absolute;width:52px;height:52px}
  .pillar--left .pillar__icon{right:-70px;top:6px}
  .pillar--right .pillar__icon{left:-72px;top:4px}
  .stack{position:absolute;left:410px;top:190px;width:300px;height:380px;border-radius:6px;background:linear-gradient(160deg,var(--stack-light),var(--stack-dark))}
  svg{fill:none;stroke:var(--body-blue);stroke-width:2.5;stroke-linecap:round;stroke-linejoin:round}
</style>
</head>
<body>
<main class="slide">
  <div class="slide__rule"></div>
  <h1 class="slide__title">Pillars of our <em>Strategy</em></h1>
  <p class="slide__subtitle">The 6 strong strategy pillars on which our business is based and flourishes</p>

  <section class="pillar pillar--left" style="left:60px;top:180px">
    <h2 class="pillar__name">Technology</h2>
    <p class="pillar__text">Adding Corvane IP to<br>expand Nexilo portfolio</p>
    <svg class="pillar__icon" viewBox="0 0 52 52"><rect x="13" y="13" width="26" height="26" rx="2"/><rect x="19" y="19" width="14" height="14"/><path d="M18 13V6M26 13V6M34 13V6M18 39v7M26 39v7M34 39v7M13 18H6M13 26H6M13 34H6M39 18h7M39 26h7M39 34h7"/></svg>
  </section>

  <section class="pillar pillar--left" style="left:60px;top:300px">
    <h2 class="pillar__name">Enter New Markets</h2>
    <p class="pillar__text">Leverage Corvane's position in<br>mobile, computing and IoT</p>
    <svg class="pillar__icon" viewBox="0 0 52 52"><circle cx="26" cy="26" r="7" fill="var(--body-blue)"/><circle cx="8" cy="26" r="3"/><circle cx="44" cy="26" r="3"/><circle cx="14" cy="10" r="3"/><circle cx="38" cy="10" r="3"/><circle cx="14" cy="42" r="3"/><circle cx="38" cy="42" r="3"/><path d="M11 26h8M33 26h8M16 12l5 8M36 12l-5 8M16 40l5-8M36 40l-5-8"/></svg>
  </section>

  <section class="pillar pillar--left" style="left:60px;top:420px">
    <h2 class="pillar__name">Mfg. &amp; Supply Chain</h2>
    <p class="pillar__text">Common manufacturing<br>Supply chain</p>
    <svg class="pillar__icon" viewBox="0 0 52 52"><circle cx="20" cy="20" r="9"/><circle cx="20" cy="20" r="3"/><path d="M20 6v5M20 29v5M6 20h5M29 20h5M10 10l4 4M30 10l-4 4M10 30l4-4"/><circle cx="36" cy="37" r="6"/><circle cx="36" cy="37" r="2"/><path d="M36 28v3M36 43v3M27 37h3M42 37h3"/></svg>
  </section>

  <div class="stack" role="img" aria-label="Six stacked isometric square frames shaded from light to dark blue, one per strategy pillar"></div>

  <section class="pillar pillar--right" style="left:830px;top:200px">
    <h2 class="pillar__name">Sales Channel</h2>
    <p class="pillar__text">Combining sales and<br>distribution channels</p>
    <svg class="pillar__icon" viewBox="0 0 52 52"><circle cx="26" cy="9" r="4"/><path d="M19 20a7 5 0 0 1 14 0z"/><circle cx="10" cy="33" r="4"/><path d="M3 44a7 5 0 0 1 14 0z"/><circle cx="42" cy="33" r="4"/><path d="M35 44a7 5 0 0 1 14 0z"/><path d="M26 24v5M26 29l-10 0M26 29l10 0"/></svg>
  </section>

  <section class="pillar pillar--right" style="left:830px;top:330px">
    <h2 class="pillar__name">Expands Footprints</h2>
    <p class="pillar__text">Increases opportunities<br>in growing markets</p>
    <svg class="pillar__icon" viewBox="0 0 52 52"><ellipse cx="15" cy="18" rx="8" ry="13"/><ellipse cx="15" cy="40" rx="6" ry="5"/><ellipse cx="37" cy="24" rx="8" ry="13"/><ellipse cx="37" cy="46" rx="6" ry="4"/></svg>
  </section>

  <section class="pillar pillar--right" style="left:830px;top:460px">
    <h2 class="pillar__name">Customer Relationships</h2>
    <p class="pillar__text">Deepens existing key<br>customer relationships<br>and adds new customers</p>
    <svg class="pillar__icon" viewBox="0 0 52 52"><path d="M2 16l8-4 6 16-8 4zM50 16l-8-4-6 16 8 4z"/><path d="M14 18l8-3 6 2 8-2"/><path d="M16 28l10 9c2 2 4 0 3-2M22 33l5 4c2 1 4-1 2-3M28 22l10 8"/><path d="M28 17l-6 6c-1 2 1 3 3 2l5-3"/></svg>
  </section>
</main>
</body>
</html>
```